FACIAL COSMETICS BUSINESS CARD

WE ARE A DENTAL PRACTICE BUT ARE OPENING UP A BRANCH FOR FACILA COSMETICS, LIKE BOTOX, FILLERS, PEELS, ETC. GWEN AND MARISOL WILL BE RUNNING THAT PART OF THE BUSINESS.
OUR CURRENT CARD IS ATTACHED AND OUR LOGO IT ATTACHED TOO. THE LOGO HAS ON IT OLMEN DENTAL, I WOULD LIKE IT TO SAY OLMEN COSMETICS, THE PHONE NUMBERS ON IT HAS TO BE REPLACED BY THE ONES I GAVE PREVIOUSLY AND THE WEB ADDRESS HAS TO BE DELETED, THE OTHER SIDE OF THE CARD HAS A MAP WHICH HAS TO BE DELETED, ADD TWO DATE-TIME LINES, I LIKE THE CARDS TO BE SIMPLE AND CLEAN, SIZE HAS TO BE NO LARGER THAN 5CMx8.5CM.
THE CARD HAS TO BE MATTE, I HATE GLOSSY, ABLE TO BE WRITTEN ON BOTH SIDES

Updates
I HAVE ATTACHED THE FILES, THEY CONSIST OF OUR CURRENT LOGO IN A FEW FORMS AND OUR BUSINESS CARD FOR THE DENTAL BRANCH, PLEASE COPY THE CURRENT DESIGN BUT ADDING THE REQUESTED CHANGES

Industry/Entity Type
Business
Contact Information for Business Card
OLMEN COSMETICS
GWEN : 0438 517 203
MARISOL : 0419 862 374
SUITE 8 HOLLOWAY COURT ARCADE
47-59 PENDRICK STREET
TALLOWMERE NSW 2389
Logo Text
OLMEN COSMETICS
Look and feel

```html
<!DOCTYPE html>
<html lang="en">
<head>
<meta charset="utf-8">
<title>Olmen Cosmetics – Business Card</title>
<link href="https://fonts.googleapis.com/css2?family=Open+Sans:ital,wght@0,600;1,600;1,700&display=swap" rel="stylesheet">
<style>
  :root {
    --page-bg: #ecebe8;
    --card-bg: #ffffff;
    --ink: #1a1a1a;
    --green: #6cbf45;
    --logo-grey: #8a8a8a;
    --logo-faint: #b9b9b9;
    --card-shadow: rgba(0, 0, 0, 0.18);
  }
  * { box-sizing: border-box; margin: 0; padding: 0; }
  html, body { width: 1200px; height: 867px; overflow: hidden; }
  body {
    background: var(--page-bg);
    font-family: "Open Sans", Arial, sans-serif;
    color: var(--ink);
    position: relative;
  }
  .card {
    position: absolute;
    width: 520px;
    height: 306px;
    background: var(--card-bg);
    border-radius: 14px;
    box-shadow: 0 6px 18px var(--card-shadow);
  }
  .card--front { left: 50px; top: 280px; }
  .card--back  { left: 630px; top: 280px; }

  /* Front */
  .brand-mark {
    position: absolute;
    left: 34px; top: 92px;
    display: flex; align-items: center; gap: 10px;
    color: var(--ink);
    font-weight: 600;
    font-size: 22px;
    letter-spacing: 1px;
    line-height: 1.05;
  }
  .brand-mark__dot {
    width: 14px; height: 14px; border-radius: 50%;
    background: var(--green);
  }
  .contact {
    position: absolute;
    left: 236px; top: 44px;
    font-style: italic;
    font-weight: 600;
    font-size: 15.5px;
    line-height: 1.3;
  }
  .contact__address { margin-bottom: 18px; }
  .contact__person { margin-bottom: 14px; }
  .contact__name {
    color: var(--green);
    font-weight: 700;
    font-size: 15px;
  }
  .contact__phone { font-size: 17px; }

  /* Back */
  .brand-faint {
    position: absolute;
    left: 0; right: 0; top: 30px;
    text-align: center;
    color: var(--logo-faint);
    font-weight: 600;
    font-size: 26px;
    letter-spacing: 2px;
  }
  .appointment {
    position: absolute;
    left: 32px; right: 32px;
  }
  .appointment--one { top: 100px; }
  .appointment--two { top: 196px; }
  .appointment__title {
    text-align: center;
    color: var(--green);
    font-weight: 600;
    font-size: 18px;
    margin-bottom: 16px;
  }
  .appointment__row {
    display: flex; align-items: baseline; gap: 8px;
    font-weight: 700;
    font-size: 17px;
  }
  .appointment__line {
    flex: 1;
    border-bottom: 2px dotted var(--green);
    height: 1px;
  }
  .appointment__line--date { flex: 1.6; margin-right: 22px; }
</style>
</head>
<body>
  <section class="card card--front" aria-label="Card front">
    <div class="brand-mark">
      <span class="brand-mark__dot"></span>
      <span>OLMEN<br>COSMETICS</span>
    </div>
    <div class="contact">
      <p class="contact__address">Suite 8, Holloway Court Arcade<br>47-59 Pendrick Street,<br>Tallowmere, NSW 2389</p>
      <div class="contact__person">
        <p class="contact__name">GWEN</p>
        <p class="contact__phone">0438 517 203</p>
      </div>
      <div class="contact__person">
        <p class="contact__name">MARISOL</p>
        <p class="contact__phone">0419 862 374</p>
      </div>
    </div>
  </section>

  <section class="card card--back" aria-label="Card back">
    <p class="brand-faint">OLMEN COSMETICS</p>
    <div class="appointment appointment--one">
      <p class="appointment__title">Appointment 1</p>
      <div class="appointment__row">
        <span>Date:</span><span class="appointment__line appointment__line--date"></span>
        <span>Time:</span><span class="appointment__line"></span>
      </div>
    </div>
    <div class="appointment appointment--two">
      <p class="appointment__title">Appointment 2</p>
      <div class="appointment__row">
        <span>Date:</span><span class="appointment__line appointment__line--date"></span>
        <span>Time:</span><span class="appointment__line"></span>
      </div>
    </div>
  </section>
</body>
</html>
```